Corporate consulting business needs a business card

I want a professional business card.... surprise me

Target Market(s)

Corprorate and Not for Profit firms and organisations

Industry/Entity Type

Consulting

Contact Information for Business Card

Logo
Strategic Advisory Services
Clear Advice, Sound Plans, Lasting Results
Tobin Averley
Director
0427 31 64 92 (Larger)
tobin@ta-advisory.com.au
www.ta-advisory.com.au
include little icons beside the contact info:

- Envelope = email
- Phone = phone
- Globe = website

Font styles to use
Serif
Sans Serif

Requirements
Must have
• Professional and clean
Nice to have
• you tell me

```html
<!DOCTYPE html>
<html lang="en">
<head>
<meta charset="utf-8">
<title>TA Advisory – Business Card</title>
<link rel="stylesheet" href="https://fonts.googleapis.com/css2?family=Crimson+Text:wght@400;600;700&display=swap">
<style>
  :root {
    --brown: #4d2c1d;
    --brown-dark: #3a2015;
    --cream: #f4efe9;
    --paper: #ffffff;
    --ink: #2b1a12;
    --stage: #e7e2dc;
  }
  * { box-sizing: border-box; margin: 0; padding: 0; }
  html, body {
    width: 1200px; height: 892px; overflow: hidden;
    background: var(--stage);
    font-family: "Crimson Text", Georgia, serif;
  }
  .canvas {
    width: 1200px; height: 892px;
    display: flex; flex-direction: column; align-items: center; justify-content: center;
    gap: 56px;
  }
  .card {
    width: 620px; height: 354px;
    position: relative;
    box-shadow: 0 6px 20px rgba(40, 20, 10, .18);
  }

  /* Shared brand lockup: circle above name */
  .brand {
    display: flex; flex-direction: column; align-items: center; gap: 8px;
  }
  .brand__circle {
    width: 56px; height: 56px; border-radius: 50%;
    border: 3px solid currentColor;
  }
  .brand__name {
    font-weight: 700; font-size: 30px; line-height: 1;
    letter-spacing: .06em; text-transform: uppercase;
  }

  /* Front */
  .card--front {
    background: var(--brown);
    color: var(--cream);
    display: flex; flex-direction: column; align-items: center; justify-content: center;
    text-align: center;
  }
  .front__rule {
    width: 320px; height: 1.5px; background: var(--cream); margin: 14px 0 12px;
  }
  .front__service, .front__tagline { font-size: 20px; line-height: 1.3; }
  .front__web { font-size: 18px; font-weight: 600; margin-top: 18px; letter-spacing: .02em; }

  /* Back */
  .card--back {
    background: var(--paper);
    color: var(--ink);
    border-right: 14px solid var(--brown);
    border-bottom: 14px solid var(--brown);
  }
  .person {
    position: absolute; left: 34px; top: 28px;
    display: flex; gap: 12px; align-items: flex-start;
  }
  .person__name { font-weight: 600; font-size: 21px; line-height: 1; }
  .person__role { font-weight: 600; font-size: 15px; margin-top: 2px; }
  .icon { width: 22px; height: 22px; flex: none; }
  .contacts {
    position: absolute; left: 34px; top: 150px;
    list-style: none; display: flex; flex-direction: column; gap: 14px;
  }
  .contacts li { display: flex; align-items: center; gap: 14px; font-weight: 600; font-size: 18px; line-height: 1; }
  .contacts .contacts__phone { font-size: 21px; }
  .brand--back {
    position: absolute; right: 40px; top: 104px;
    color: var(--brown-dark);
  }
  .brand--back .brand__circle { width: 46px; height: 46px; border-width: 2.5px; }
  .brand--back .brand__name { font-size: 25px; }
</style>
</head>
<body>
<main class="canvas">
  <section class="card card--front" aria-label="Card front">
    <div class="brand">
      <span class="brand__circle"></span>
      <span class="brand__name">TA Advisory</span>
    </div>
    <div class="front__rule"></div>
    <p class="front__service">Strategic Advisory Services</p>
    <p class="front__tagline">Clear Advice, Sound Plans, Lasting Results</p>
    <p class="front__web">www.ta-advisory.com.au</p>
  </section>

  <section class="card card--back" aria-label="Card back">
    <div class="person">
      <svg class="icon" viewBox="0 0 22 22" aria-hidden="true">
        <circle cx="11" cy="11" r="10.5" fill="var(--ink)"/>
        <circle cx="11" cy="8.5" r="3.2" fill="#fff"/>
        <path d="M5 17c1-3.2 3.3-4.6 6-4.6s5 1.4 6 4.6z" fill="#fff"/>
      </svg>
      <div>
        <p class="person__name">Tobin Averley</p>
        <p class="person__role">Director</p>
      </div>
    </div>

    <ul class="contacts">
      <li class="contacts__phone">
        <svg class="icon" viewBox="0 0 22 22" aria-hidden="true">
          <circle cx="11" cy="11" r="10" fill="none" stroke="var(--ink)" stroke-width="1.4"/>
          <path d="M8 6.5l1.6 2.6-1 1.1c.6 1.4 1.7 2.5 3.2 3.2l1.1-1 2.6 1.6-.8 1.6c-3.7-.3-7-3.6-7.3-7.3z" fill="var(--ink)"/>
        </svg>
        0427 31 64 92
      </li>
      <li>
        <svg class="icon" viewBox="0 0 22 22" aria-hidden="true">
          <circle cx="11" cy="11" r="10" fill="none" stroke="var(--ink)" stroke-width="1.4"/>
          <rect x="6" y="7.5" width="10" height="7" fill="none" stroke="var(--ink)" stroke-width="1.3"/>
          <path d="M6 7.5l5 4 5-4" fill="none" stroke="var(--ink)" stroke-width="1.3"/>
        </svg>
        tobin@ta-advisory.com.au
      </li>
      <li>
        <svg class="icon" viewBox="0 0 22 22" aria-hidden="true">
          <circle cx="11" cy="11" r="10" fill="none" stroke="var(--ink)" stroke-width="1.4"/>
          <circle cx="11" cy="11" r="5.5" fill="none" stroke="var(--ink)" stroke-width="1.2"/>
          <ellipse cx="11" cy="11" rx="2.3" ry="5.5" fill="none" stroke="var(--ink)" stroke-width="1"/>
          <path d="M5.5 11h11" stroke="var(--ink)" stroke-width="1"/>
        </svg>
        www.ta-advisory.com.au
      </li>
    </ul>

    <div class="brand brand--back">
      <span class="brand__circle"></span>
      <span class="brand__name">TA Advisory</span>
    </div>
  </section>
</main>
</body>
</html>
```